PawNook business card

Looking for a fun and cool biz card for a new company with patent pending products. I have products to help and protect dogs hearing. My colors are pantone blue and orange.
Updates

Please add tag line: Protect the ones you love...even your PawNooks!

Target Market(s)

Animal/Dog lovers!

Industry/Entity Type

Retail

Contact Information for Business Card

I'm looking for something simple yet fun with all the info included for biz cards

Colors
0555a3
f78f20

Requirements
Must have
• Logo
Nice to have
• name, website and email
Should not have
• phone number

```html
<!DOCTYPE html>
<html lang="en">
<head>
<meta charset="UTF-8">
<title>PawNook Business Card</title>
<link href="https://fonts.googleapis.com/css2?family=Roboto:ital,wght@0,400;0,700;0,900;1,400&display=swap" rel="stylesheet">
<style>
  :root {
    --navy: #1f2b4f;
    --orange: #f15a22;
    --white: #ffffff;
    --mist: #c9d0e3;
    --backdrop: #e9e7e3;
    --photo-warm: #d9b48a;
    --photo-light: #f3e6d6;
  }
  * { margin: 0; padding: 0; box-sizing: border-box; }
  html, body {
    width: 1200px;
    height: 800px;
    overflow: hidden;
    background: var(--backdrop);
    font-family: "Roboto", Arial, sans-serif;
  }
  .sheet {
    position: relative;
    width: 1200px;
    height: 800px;
  }
  .card {
    position: absolute;
    top: 245px;
    width: 540px;
    height: 310px;
    border-radius: 4px;
    overflow: hidden;
    box-shadow: 0 10px 28px rgba(0, 0, 0, 0.18);
  }
  .card--back {
    left: 40px;
    background: var(--navy);
    display: flex;
    flex-direction: column;
    align-items: center;
    justify-content: center;
    gap: 22px;
  }
  .card--front {
    left: 620px;
    background: var(--navy);
  }
  .brand-name {
    font-weight: 900;
    color: var(--orange);
    letter-spacing: 0.5px;
    line-height: 1;
  }
  .card--back .brand-name { font-size: 76px; }
  .tagline {
    font-size: 16px;
    font-style: italic;
    color: var(--mist);
    text-align: center;
  }

  .front-top {
    position: absolute;
    left: 0; top: 0;
    width: 100%;
    height: 128px;
    background: var(--white);
  }
  .front-top .brand-name {
    position: absolute;
    left: 34px;
    top: 36px;
    font-size: 64px;
  }
  .front-photo {
    position: absolute;
    right: 24px;
    top: 10px;
    width: 130px;
    height: 118px;
    background: radial-gradient(circle at 50% 50%, var(--photo-light) 0%, var(--photo-warm) 70%, var(--white) 100%);
  }
  .front-band {
    position: absolute;
    left: 0; top: 128px;
    width: 100%;
    height: 9px;
    background: var(--orange);
  }
  .holder-name {
    position: absolute;
    left: 34px;
    top: 154px;
    font-size: 21px;
    font-weight: 700;
    color: var(--orange);
  }
  .contact-list {
    position: absolute;
    left: 34px;
    top: 194px;
    list-style: none;
  }
  .contact-item {
    display: flex;
    align-items: center;
    gap: 12px;
    height: 28px;
    font-size: 15px;
    color: var(--white);
  }
  .contact-icon {
    width: 18px;
    height: 18px;
    flex: none;
  }
</style>
</head>
<body>
<main class="sheet">
  <section class="card card--back" aria-label="Card back">
    <span class="brand-name">PawNook</span>
    <p class="tagline">Protect the ones you love...even your PawNooks!</p>
  </section>

  <section class="card card--front" aria-label="Card front">
    <div class="front-top">
      <span class="brand-name">PawNook</span>
      <div class="front-photo" role="img" aria-label="Photo of a small happy dog with one ear raised"></div>
    </div>
    <div class="front-band"></div>
    <p class="holder-name">Marc Delorme</p>
    <ul class="contact-list">
      <li class="contact-item">
        <svg class="contact-icon" viewBox="0 0 18 18" aria-hidden="true">
          <circle cx="9" cy="9" r="9" fill="var(--orange)"/>
          <rect x="4.5" y="5.8" width="9" height="6.4" rx="1" fill="var(--white)"/>
          <path d="M4.8 6.2 9 9.3l4.2-3.1" fill="none" stroke="var(--orange)" stroke-width="1"/>
        </svg>
        marc@pawnook.com
      </li>
      <li class="contact-item">
        <svg class="contact-icon" viewBox="0 0 18 18" aria-hidden="true">
          <circle cx="9" cy="9" r="9" fill="var(--orange)"/>
          <g fill="none" stroke="var(--white)" stroke-width="1.1">
            <circle cx="9" cy="9" r="4.5"/>
            <ellipse cx="9" cy="9" rx="2" ry="4.5"/>
            <path d="M4.5 9h9"/>
          </g>
        </svg>
        www.pawnook.com
      </li>
    </ul>
  </section>
</main>
</body>
</html>
```